Korbin Ventilation's. "We're Miles above the rest"!

Good day< Does your company do face mask? that is question 1. and lets finish the stationary design and I will pay for that now? 2 If your company has BLACK HATS now I would want to do some of those? 3 I notice do you do BANNER'S and or something I can put on van's magnet type or on a building! )k that's enough but for now lets start with the stationary stuff? let me know you should have my information, and the design look's GREAT!!! Thank you..

```html
<!DOCTYPE html>
<html lang="en">
<head>
<meta charset="utf-8">
<title>Korbin Ventilation's – Letterhead</title>
<link rel="stylesheet" href="https://fonts.googleapis.com/css2?family=Montserrat:wght@400;500;600;700&display=swap">
<style>
  :root {
    --backdrop: #d4d4d4;
    --paper: #ffffff;
    --ink: #111111;
    --band-dark: #0d0d0d;
    --band-mid: #2b2b2b;
    --accent-grey: #b4b4b4;
    --text-body: #1e1e1e;
    --text-muted: #3a3a3a;
  }
  * { box-sizing: border-box; margin: 0; padding: 0; }
  html, body {
    width: 837px; height: 1200px; overflow: hidden;
    background: var(--backdrop);
    font-family: "Montserrat", Arial, sans-serif;
  }
  .letterhead {
    position: absolute; left: 28px; top: 48px;
    width: 780px; height: 1103px;
    background: var(--paper);
    box-shadow: 0 4px 14px rgba(0,0,0,.18);
    overflow: hidden;
  }
  .wave { position: absolute; left: 0; width: 780px; }
  .wave--top { top: 0; height: 260px; }
  .wave--bottom { bottom: 0; height: 150px; }

  .brand {
    position: absolute; left: 82px; top: 250px; width: 230px;
    display: flex; flex-direction: column; align-items: center; gap: 12px;
  }
  .brand__dot { width: 62px; height: 62px; border-radius: 50%; background: var(--ink); }
  .brand__name {
    font-weight: 700; font-size: 21px; color: var(--ink);
    text-align: center; line-height: 1.15;
  }

  .contact { position: absolute; left: 442px; top: 221px; color: var(--ink); }
  .contact__name { font-weight: 700; font-size: 19.5px; letter-spacing: .3px; }
  .contact__role { font-weight: 500; font-size: 12.5px; margin-top: 3px; }
  .contact__list { list-style: none; margin-top: 16px; }
  .contact__item {
    display: flex; align-items: flex-start; gap: 11px;
    font-weight: 500; font-size: 14px; line-height: 1.25; margin-bottom: 6px;
  }
  .contact__item svg { width: 14px; height: 14px; flex: none; margin-top: 2px; }
  .contact__item--address { margin-top: 4px; }

  .sender { position: absolute; left: 82px; top: 403px; color: var(--ink); }
  .sender__name { font-weight: 700; font-size: 20px; letter-spacing: .3px; }
  .sender__role { font-size: 12.5px; color: var(--text-muted); margin-top: 6px; letter-spacing: .2px; }

  .letter-body {
    position: absolute; left: 82px; top: 480px; width: 628px;
    font-size: 11.4px; line-height: 15.6px; color: var(--text-body);
    text-align: justify;
  }
  .letter-body p + p { margin-top: 15px; }

  .signoff { position: absolute; right: 70px; top: 905px; text-align: left; width: 170px; }
  .signoff__name { font-weight: 700; font-size: 15px; color: var(--ink); letter-spacing: .3px; }
  .signoff__signature {
    margin-top: 8px; width: 168px; height: 30px;
    background: linear-gradient(90deg, #e9e9e9, #f4f4f4);
    border-radius: 3px;
  }

  .footer-web {
    position: absolute; right: 75px; bottom: 30px;
    color: #ffffff; font-weight: 600; font-size: 13.5px; letter-spacing: .2px;
  }
</style>
</head>
<body>
<main class="letterhead">
  <svg class="wave wave--top" viewBox="0 0 780 260" preserveAspectRatio="none" aria-hidden="true">
    <defs>
      <linearGradient id="bandTop" x1="0" y1="0" x2="1" y2="0.3">
        <stop offset="0" stop-color="var(--band-dark)"/>
        <stop offset="0.6" stop-color="#1a1a1a"/>
        <stop offset="1" stop-color="var(--band-mid)"/>
      </linearGradient>
    </defs>
    <rect width="780" height="260" fill="url(#bandTop)"/>
    <path d="M0,175 C140,60 320,55 470,110 C600,158 700,235 780,165 L780,260 L0,260 Z" fill="var(--accent-grey)"/>
    <path d="M0,192 C140,78 320,73 470,128 C600,176 700,252 780,185 L780,260 L0,260 Z" fill="var(--paper)"/>
    <path d="M470,210 C600,215 700,240 780,175 L780,180 C700,252 600,200 470,210 Z" fill="var(--paper)"/>
  </svg>

  <div class="brand">
    <span class="brand__dot"></span>
    <span class="brand__name">Korbin Ventilation's</span>
  </div>

  <section class="contact">
    <h1 class="contact__name">DALE HARMON</h1>
    <p class="contact__role">Korbin heating &amp; air conditioning</p>
    <ul class="contact__list">
      <li class="contact__item">
        <svg viewBox="0 0 16 16"><path d="M3 1.5l3 .5 1 3-1.8 1.3a9 9 0 0 0 4.5 4.5L11 9l3 1 .5 3-2 1.5C6.5 14 2 9.5 1.5 3.5z" fill="none" stroke="#111" stroke-width="1.4" stroke-linejoin="round"/></svg>
        (720) 555-0148
      </li>
      <li class="contact__item">
        <svg viewBox="0 0 16 16"><path d="M1 5c2-3 12-3 14 0v2h-4V5.5H5V7H1z" fill="#111"/><rect x="3" y="8" width="10" height="6" rx="1" fill="#111"/></svg>
        (303) 555-0172
      </li>
      <li class="contact__item">
        <svg viewBox="0 0 16 16"><rect x="1" y="3" width="14" height="10" fill="#111"/><path d="M1.5 3.5L8 9l6.5-5.5M1.5 12.5l5-4.5M14.5 12.5l-5-4.5" stroke="#fff" stroke-width="1.1" fill="none"/></svg>
        daleharmon@korbinair.com
      </li>
      <li class="contact__item">
        <svg viewBox="0 0 16 16" fill="none" stroke="#111" stroke-width="1.3"><circle cx="8" cy="8" r="6.5"/><ellipse cx="8" cy="8" rx="3" ry="6.5"/><path d="M1.5 8h13M2.5 4.5h11M2.5 11.5h11"/></svg>
        www.korbinheating.com
      </li>
      <li class="contact__item contact__item--address">
        <svg viewBox="0 0 16 16"><path d="M8 1a5 5 0 0 0-5 5c0 4 5 9 5 9s5-5 5-9a5 5 0 0 0-5-5z" fill="#111"/><circle cx="8" cy="6" r="1.8" fill="#fff"/></svg>
        <span>1850 Larkspur Ave Denver,<br>Colorado 80219</span>
      </li>
    </ul>
  </section>

  <section class="sender">
    <h2 class="sender__name">DALE HARMON</h2>
    <p class="sender__role">KORBIN HEATING &amp; AIR CONDITIONING</p>
  </section>

  <article class="letter-body">
    <p>Contrary to popular belief, Lorem Ipsum is not simply random text. It has roots in a piece of classical Latin literature from 45 BC, making it over 2000 years old. Richard McClintock, a Latin professor at Hampden-Sydney College in Virginia, looked up one of the more obscure Latin words, consectetur, from a Lorem Ipsum passage, and going through the cites of the word in classical literature, discovered the undoubtable source. Lorem Ipsum comes from sections 1.10.32 and 1.10.33 of "de Finibus Bonorum et Malorum" (The Extremes of Good and Evil) by Cicero, written in 45 BC. This book is a treatise on the theory of ethics, very popular during the Renaissance. The first line of Lorem Ipsum, "Lorem ipsum dolor sit amet..", comes from a line in section 1.10.32.The standard chunk of Lorem Ipsum used since the 1500s is reproduced below for those interested. Sections 1.10.32 and 1.10.33 from "de Finibus Bonorum et Malorum" by Cicero are also reproduced in their exact original form, accompanied by English versions from the 1914 translation by H. Rackham.</p>
    <p>It is a long established fact that a reader will be distracted by the readable content of a page when looking at its layout. The point of using Lorem Ipsum is that it has a more-or-less normal distribution of letters, as opposed to using 'Content here, content here', making it look like readable English. Many desktop publishing packages and web page editors now use Lorem Ipsum as their default model text, and a search for 'lorem ipsum' will uncover many web sites still in their infancy. Various versions have evolved over the years, sometimes by accident, sometimes on purpose (injected humour and the like).</p>
    <p>The standard chunk of Lorem Ipsum used since the 1500s is reproduced below for those interested. Sections 1.10.32 and 1.10.33 from "de Finibus Bonorum et Malorum" by Cicero are also reproduced in their exact original form, accompanied by English versions from the 1914 translation by H. Rackham. Contrary to popular belief,</p>
  </article>

  <div class="signoff">
    <p class="signoff__name">DALE HARMON</p>
    <div class="signoff__signature" role="img" aria-label="Handwritten signature of Dale Harmon"></div>
  </div>

  <svg class="wave wave--bottom" viewBox="0 0 780 150" preserveAspectRatio="none" aria-hidden="true">
    <defs>
      <linearGradient id="bandBottom" x1="0" y1="0" x2="1" y2="0">
        <stop offset="0" stop-color="var(--band-dark)"/>
        <stop offset="1" stop-color="var(--band-mid)"/>
      </linearGradient>
    </defs>
    <path d="M0,50 C150,5 300,80 470,95 C610,108 700,20 780,60 L780,150 L0,150 Z" fill="var(--accent-grey)"/>
    <path d="M0,68 C150,22 300,96 470,112 C610,124 700,40 780,78 L780,150 L0,150 Z" fill="url(#bandBottom)"/>
  </svg>
  <p class="footer-web">www.korbinventilation.com</p>
</main>
</body>
</html>
```